Congressional Website with splash page for Texas Democratic Black Woman

I would like a splash page with a turquoise shaded theme to it. My logo can be played with but the original logo is black white and red... we are now wanting a page that is in shades of turquoise with the black white and red colors. On the splash page, I want to collect volunteer information and prompt people to donate. I would like to.just have a large picture of me of some sort and then you have to click to enter the rest of the page with the issues.

Target Market(s)

Voters and Donors and democrats

Industry/Entity Type

campaign/elections

Coding

Coded - Design and coding required

Number of Pages Required

2 page

Font styles to use
Serif

Colors
0094D4
00A9DD
6FCCEA
C7EBF8
E9F6FB

Requirements
Must have
• I must have a landing page... and then it open up to the other pages.

```html
<!DOCTYPE html>
<html lang="en">
<head>
<meta charset="utf-8">
<title>Nadia Brentwood — Democrat for US Congress</title>
<link rel="stylesheet" href="https://fonts.googleapis.com/css2?family=Oswald:wght@300;400;500&family=Lato:wght@400&display=swap">
<style>
  :root {
    --turquoise-deep: #0094D4;
    --turquoise: #00A9DD;
    --turquoise-light: #6FCCEA;
    --turquoise-pale: #C7EBF8;
    --ink: #000000;
    --paper: #FFFFFF;
    --alert-red: #FF0019;
    --overlay-shadow: #0B6FB3;
  }
  * { box-sizing: border-box; margin: 0; padding: 0; }
  html, body { width: 1200px; height: 738px; overflow: hidden; }
  body { font-family: "Lato", sans-serif; color: var(--paper); background: var(--turquoise-deep); }

  .splash { position: relative; width: 1200px; height: 738px; overflow: hidden; }

  .splash__portrait {
    position: absolute; inset: 0;
    background:
      radial-gradient(ellipse 220px 360px at 600px 380px, var(--overlay-shadow) 0%, rgba(11,111,179,0) 100%),
      linear-gradient(180deg, #2A9BE0 0%, var(--turquoise-deep) 45%, #1E93DB 100%);
  }

  .brand { position: absolute; left: 74px; top: 42px; width: 326px; }
  .brand__name {
    font-family: "Oswald", sans-serif; font-weight: 400; font-size: 46px;
    line-height: 1; letter-spacing: 1px; color: var(--paper); white-space: nowrap;
  }
  .brand__tagline {
    margin-top: 34px; padding: 9px 0 7px;
    border-top: 3px solid var(--paper); border-bottom: 3px solid var(--paper);
    font-family: "Oswald", sans-serif; font-weight: 500; font-size: 21px;
    letter-spacing: 1.2px; text-align: center; line-height: 1.1;
  }

  .actions { position: absolute; top: 80px; left: 739px; display: flex; gap: 10px; }
  .btn {
    display: inline-flex; align-items: center; justify-content: center;
    height: 52px; font-family: "Oswald", sans-serif; font-weight: 300;
    font-size: 19px; letter-spacing: 0.6px; color: var(--paper); text-decoration: none;
  }
  .btn--outline { width: 228px; border: 2px solid var(--paper); }
  .btn--dark { width: 140px; background: var(--ink); }
  .btn--enter {
    position: absolute; left: 616px; top: 463px; width: 177px; height: 57px;
    background: var(--alert-red); font-weight: 400; font-size: 21px;
  }

  .headline {
    position: absolute; left: 74px; top: 318px;
    font-family: "Oswald", sans-serif; font-weight: 300; font-size: 66px;
    line-height: 74px; letter-spacing: 0.5px; text-transform: uppercase;
  }

  .issue { position: absolute; left: 616px; top: 288px; width: 520px; }
  .issue__title {
    font-family: "Oswald", sans-serif; font-weight: 300; font-size: 38px;
    line-height: 46px; letter-spacing: 0.5px; text-transform: uppercase;
  }
  .issue__text { margin-top: 8px; font-size: 20px; line-height: 33px; letter-spacing: 0.3px; }

  .footer {
    position: absolute; left: 0; right: 0; top: 665px; height: 73px;
    border-top: 1px solid var(--turquoise-pale);
  }
  .footer__copyright { position: absolute; left: 74px; top: 29px; font-size: 13px; }
  .social { position: absolute; right: 72px; top: 24px; display: flex; gap: 14px; list-style: none; }
  .social__item {
    display: flex; align-items: center; gap: 5px;
    font-family: "Lato", sans-serif; font-size: 12px; color: var(--paper);
  }
  .social__dot { width: 8px; height: 8px; border-radius: 50%; background: var(--paper); }
</style>
</head>
<body>
<main class="splash">
  <div class="splash__portrait" role="img" aria-label="Portrait of the candidate seated on a wooden bench, smiling, toned in turquoise"></div>

  <header class="brand">
    <div class="brand__name">NADIA BRENTWOOD</div>
    <div class="brand__tagline">DEMOCRAT FOR US CONGRESS</div>
  </header>

  <nav class="actions">
    <a class="btn btn--outline" href="#volunteer">VOLUNTEER INFORMATION</a>
    <a class="btn btn--dark" href="#donate">DONATE</a>
  </nav>

  <h1 class="headline">Texas Democratic<br>Black Woman</h1>

  <section class="issue">
    <h2 class="issue__title">Voting Rights</h2>
    <p class="issue__text">Representative Nadia Brentwood has been a prominent voice for voting rights at the state and federal levels.</p>
  </section>

  <a class="btn btn--enter" href="#issues">ENTER NOW</a>

  <footer class="footer">
    <p class="footer__copyright">Copyright © 2021. Company Name All Right Reserved</p>
    <ul class="social">
      <li class="social__item"><span class="social__dot"></span>Friendlane</li>
      <li class="social__item"><span class="social__dot"></span>Snapsy</li>
      <li class="social__item"><span class="social__dot"></span>Chirply</li>
      <li class="social__item"><span class="social__dot"></span>Worknet</li>
      <li class="social__item"><span class="social__dot"></span>Vidstream</li>
    </ul>
  </footer>
</main>
</body>
</html>
```